Music Festival Business Cards

The Lanternmoor Festival
Produced by Bramblewick Sound Group LLC
New music festival in Arkansas.

Target Market(s)

18-35 year olds

Industry/Entity Type

Festival

Contact Information for Business Card

We are a 5-partner team producing a music festival in Arkansas. We need slick business cards, and I want them to be square.

Requirements
Must have
• I NEED THESE TO BE IN SQUARE SIZE - 2x2 or 2.5x2.5... please not regular size.
• I need www.thelanternmoor.live as the link to website.

```html
<!DOCTYPE html>
<html lang="en">
<head>
<meta charset="utf-8">
<title>The Lanternmoor Festival – Business Card</title>
<link rel="stylesheet" href="https://fonts.googleapis.com/css2?family=Open+Sans:wght@400;600&display=swap">
<style>
  :root {
    --teal: #33cbd3;
    --frost: #eef1f2;
    --backdrop: #e2e4e6;
    --white: #ffffff;
  }
  html, body {
    margin: 0;
    padding: 0;
    width: 1200px;
    height: 900px;
    overflow: hidden;
    background: var(--backdrop);
    font-family: "Open Sans", Arial, sans-serif;
  }
  .card {
    position: absolute;
    left: 330px;
    top: 180px;
    width: 540px;
    height: 540px;
  }
  .card-shape {
    position: absolute;
    inset: 0;
  }
  .holder {
    position: absolute;
    left: 32px;
    color: var(--white);
    line-height: 1;
    white-space: nowrap;
  }
  .holder-name {
    top: 44px;
    font-size: 26px;
    font-weight: 400;
  }
  .holder-role {
    top: 78px;
    font-size: 17px;
    font-weight: 400;
  }
  .contact-list {
    position: absolute;
    left: 32px;
    top: 428px;
    margin: 0;
    padding: 0;
    list-style: none;
    color: var(--white);
    font-size: 17px;
    white-space: nowrap;
  }
  .contact-item {
    display: flex;
    align-items: center;
    height: 26px;
  }
  .contact-icon {
    width: 14px;
    height: 14px;
    margin-right: 11px;
    flex: none;
  }
  .brand-name {
    position: absolute;
    left: 190px;
    width: 340px;
    top: 272px;
    text-align: center;
    color: var(--teal);
    font-size: 24px;
    font-weight: 600;
    letter-spacing: 2px;
    line-height: 1;
    white-space: nowrap;
  }
</style>
</head>
<body>
  <main class="card">
    <svg class="card-shape" width="540" height="540" viewBox="0 0 540 540" aria-hidden="true">
      <rect x="0" y="0" width="540" height="540" fill="var(--frost)"/>
      <rect class="band-top" x="0" y="0" width="540" height="135" fill="var(--teal)"/>
      <rect class="band-bottom" x="0" y="395" width="540" height="145" fill="var(--teal)"/>
      <circle class="brand-disc" cx="360" cy="240" r="168" fill="var(--frost)" stroke="var(--teal)" stroke-width="4"/>
    </svg>

    <div class="holder holder-name">Marcus Ellery</div>
    <div class="holder holder-role">Managing Director</div>

    <div class="brand-name">THE LANTERNMOOR</div>

    <ul class="contact-list">
      <li class="contact-item">
        <svg class="contact-icon" viewBox="0 0 24 24" aria-hidden="true"><path fill="#fff" d="M6.6 10.8a15.1 15.1 0 0 0 6.6 6.6l2.2-2.2c.3-.3.7-.4 1-.2 1.1.4 2.3.6 3.6.6.6 0 1 .4 1 1V20c0 .6-.4 1-1 1A17 17 0 0 1 3 4c0-.6.4-1 1-1h3.5c.6 0 1 .4 1 1 0 1.3.2 2.5.6 3.6.1.3 0 .7-.2 1z"/></svg>
        044-555 010 246
      </li>
      <li class="contact-item">
        <svg class="contact-icon" viewBox="0 0 24 24" aria-hidden="true"><path fill="#fff" d="M2 5h20v14H2z"/><path fill="none" stroke="var(--teal)" stroke-width="1.6" d="M2.5 5.5 12 12l9.5-6.5"/></svg>
        hello@thelanternmoor.live
      </li>
      <li class="contact-item">
        <svg class="contact-icon" viewBox="0 0 24 24" aria-hidden="true"><g fill="none" stroke="#fff" stroke-width="2.6" stroke-linecap="round"><path d="M10 14a5 5 0 0 0 7 0l3-3a5 5 0 0 0-7-7l-1.5 1.5"/><path d="M14 10a5 5 0 0 0-7 0l-3 3a5 5 0 0 0 7 7l1.5-1.5"/></g></svg>
        www.thelanternmoor.live
      </li>
    </ul>
  </main>
</body>
</html>
```